Business Card Design - Law Firm

We are a boutique law firm located near the beach in Manly, Australia. We have recently had a new logo designed and are revamping our business cards with the new logo.

We have recently had a business card design done for us but are not entirely happy with it. We are looking for something modern, simplistic but striking. We would like to see multiple designs.

We have attached a word document which includes our new logo and the current business card design which we are looking at moving away from.

We would like the business cards to be double sided. We would like the design to include something which we can print in gloss colour when we send it to the business card printers.

```html
<!DOCTYPE html>
<html lang="en">
<head>
<meta charset="utf-8">
<title>Harbourne &amp; Associates – Business Card</title>
<link href="https://fonts.googleapis.com/css2?family=Arimo:wght@400;700&display=swap" rel="stylesheet">
<style>
  :root {
    --stage: #a4a4a6;
    --card-dark: #1c1b1c;
    --card-light: #ffffff;
    --brand-blue: #2c3b8f;
    --brand-gold: #c3a86a;
    --text-grey: #505050;
    --rule-grey: #9a9a9a;
    --on-dark: #f2f2f2;
  }
  * { box-sizing: border-box; margin: 0; padding: 0; }
  html, body {
    width: 1200px; height: 1200px; overflow: hidden;
    background: var(--stage);
    font-family: "Arimo", Arial, sans-serif;
  }
  .sheet {
    width: 1200px; height: 1200px;
    display: flex; flex-direction: column; align-items: center; justify-content: center;
    gap: 56px;
  }
  .card {
    width: 880px; height: 512px;
    position: relative;
    box-shadow: 0 6px 18px rgba(0,0,0,.25);
  }
  .card--front { background: var(--card-dark); display: flex; align-items: center; justify-content: center; }
  .card--back { background: var(--card-light); }

  .firm-name {
    display: flex; align-items: center; gap: 14px;
    font-weight: 700; letter-spacing: .06em;
    white-space: nowrap;
  }
  .firm-name__dot { width: 16px; height: 16px; border-radius: 50%; background: var(--brand-blue); flex: none; }
  .card--front .firm-name { color: var(--on-dark); font-size: 24px; }
  .card--back .firm-name { color: #2a2a2a; font-size: 19px; }

  .card--back .firm-name {
    position: absolute; left: 72px; top: 246px;
  }
  .divider {
    position: absolute; left: 448px; top: 150px; width: 1px; height: 212px;
    background: var(--rule-grey);
  }
  .contact {
    position: absolute; left: 486px; top: 150px;
    color: var(--text-grey);
  }
  .contact__name { color: var(--brand-blue); font-size: 38px; font-weight: 400; line-height: 1; }
  .contact__role { font-size: 19px; margin-top: 6px; }
  .contact__address { font-size: 19px; line-height: 1.2; margin-top: 26px; }
  .contact__lines { list-style: none; margin-top: 24px; font-size: 19px; }
  .contact__lines li { display: flex; align-items: center; gap: 10px; line-height: 1.3; }
  .contact__lines svg { width: 22px; height: 20px; flex: none; }
</style>
</head>
<body>
<main class="sheet">
  <section class="card card--front" aria-label="Card front">
    <div class="firm-name"><span class="firm-name__dot"></span>Harbourne &amp; Associates Lawyers</div>
  </section>

  <section class="card card--back" aria-label="Card back">
    <div class="firm-name"><span class="firm-name__dot"></span>Harbourne &amp; Associates Lawyers</div>
    <div class="divider"></div>
    <div class="contact">
      <h1 class="contact__name">Nina Calloway</h1>
      <p class="contact__role">Practice Manager</p>
      <p class="contact__address">Suite 4, 12 Tidewater Lane<br>CORALBAY NSW 2190</p>
      <ul class="contact__lines">
        <li>
          <svg viewBox="0 0 22 20" aria-hidden="true"><path d="M4 3c-2 2-1 6 3 10s8 5 10 3l1-2-3-2-2 1c-2-1-4-3-5-5l1-2-2-3z" fill="var(--brand-gold)"/></svg>
          (02) 5550 1847
        </li>
        <li>
          <svg viewBox="0 0 22 20" aria-hidden="true"><rect x="2" y="4" width="18" height="12" fill="none" stroke="var(--brand-gold)" stroke-width="1.6"/><path d="M2 4l9 7 9-7M2 16l7-6M20 16l-7-6" fill="none" stroke="var(--brand-gold)" stroke-width="1.4"/></svg>
          nina.calloway@coralbaylaw.com.au
        </li>
        <li>
          <svg viewBox="0 0 22 20" aria-hidden="true"><g fill="none" stroke="var(--brand-gold)" stroke-width="1.4"><circle cx="11" cy="10" r="8"/><ellipse cx="11" cy="10" rx="3.5" ry="8"/><path d="M3 10h16M4.5 5.5h13M4.5 14.5h13"/></g></svg>
          www.harbourneassociates.com.au
        </li>
      </ul>
    </div>
  </section>
</main>
</body>
</html>
```